Premium Olive Oil Bottle Label

Need a double bottle label for our premium olive oil (front and back). Please refer to the brief attached. The label needs to incorporate the elements from the logo designs that we provide in attachment into a single design language. The front panel should capture attention and the back panel provide a story of our unique product.

Target Market(s)

US and Europe

Industry/Entity Type

Food Production

Font styles to use
Other font styles liked:
• Please refer to the Brief

Colors

Designer to choose colors to be used in the design.

Requirements
Must have
• Integrate the elements in the brief into a single premium execution.
Nice to have
• Feel free to use the provided visual elements as a base for your further creative exploration.
Should not have
• Too many colors. Please propose a restricted color palette as the bottle is black matte. The design needs to deliver premium appeal and be distinctive.

```html
<!DOCTYPE html>
<html lang="en">
<head>
<meta charset="utf-8">
<title>Le Haut Verger – Olive Oil Label, Front and Back</title>
<link rel="stylesheet" href="https://fonts.googleapis.com/css2?family=Josefin+Sans:wght@400;600&display=swap">
<style>
  :root {
    --bottle-black: #000000;
    --gold: #c9a862;
    --gold-deep: #8d6a32;
    --line-white: #e8e6e1;
    --text-soft: #d9d7d2;
  }
  html, body {
    margin: 0;
    padding: 0;
    width: 1200px;
    height: 1200px;
    overflow: hidden;
    background: var(--bottle-black);
  }
  .canvas {
    position: relative;
    width: 1200px;
    height: 1200px;
    background: var(--bottle-black);
    font-family: "Josefin Sans", sans-serif;
  }
  .front-label {
    position: absolute;
    left: 0;
    top: 0;
    width: 800px;
    height: 1200px;
  }
  .back-label {
    position: absolute;
    left: 720px;
    top: 170px;
    width: 272px;
    height: 860px;
    text-align: center;
    color: var(--text-soft);
  }
  .back-ornament {
    position: absolute;
    left: 12px;
    width: 248px;
    background: linear-gradient(180deg, #15130f, #221e16 50%, #15130f);
  }
  .back-ornament.top { top: 4px; height: 14px; border-radius: 6px; }
  .back-ornament.bottom { top: 778px; height: 76px; border-radius: 14px 14px 30px 30px; }
  .back-brand {
    position: absolute;
    left: 0;
    right: 0;
    top: 28px;
  }
  .back-brand .mark {
    display: block;
    width: 36px;
    height: 36px;
    margin: 0 auto 12px;
    border-radius: 50%;
    background: var(--gold);
  }
  .back-brand .name {
    font-weight: 600;
    font-size: 21px;
    letter-spacing: 1.2px;
    color: var(--gold);
    line-height: 1;
  }
  .back-brand .origin {
    margin-top: 5px;
    font-size: 8.5px;
    letter-spacing: 1.2px;
    color: var(--gold);
  }
  .story-title {
    position: absolute;
    left: 0;
    right: 0;
    top: 165px;
    margin: 0;
    font-weight: 400;
    font-size: 9.5px;
    letter-spacing: 1.6px;
    color: var(--line-white);
  }
  .story-body {
    position: absolute;
    left: 0;
    right: 0;
    top: 205px;
    margin: 0;
    font-size: 7px;
    line-height: 17.8px;
    letter-spacing: 1px;
    text-transform: uppercase;
  }
  .meta {
    position: absolute;
    left: 0;
    right: 0;
    margin: 0;
    font-size: 7px;
    line-height: 17.8px;
    letter-spacing: 1px;
    text-transform: uppercase;
  }
  .meta.date { top: 544px; }
  .meta.best-before { top: 579px; }
  .meta.contact { top: 668px; }
  .meta.volume {
    top: 737px;
    font-size: 9.5px;
    line-height: 16px;
    letter-spacing: 0.3px;
    color: var(--line-white);
  }
</style>
</head>
<body>
<main class="canvas">

  <section class="front-label" aria-label="Front label">
    <svg width="800" height="1200" viewBox="0 0 800 1200" xmlns="http://www.w3.org/2000/svg">
      <defs>
        <radialGradient id="ornament-fill" cx="50%" cy="50%" r="55%">
          <stop offset="0%" stop-color="#0c0b09"/>
          <stop offset="70%" stop-color="#1d1a14"/>
          <stop offset="100%" stop-color="#2a261d"/>
        </radialGradient>
        <path id="top-arc" d="M 236 470 A 168 160 0 0 1 572 470"/>
        <path id="bottom-arc" d="M 262 790 A 142 100 0 0 0 546 790"/>
        <path id="artisanal-path" d="M 280 790 Q 310 815 350 832"/>
        <path id="unfiltered-path" d="M 458 832 Q 500 815 530 785"/>
      </defs>

      <g class="ornament-field" role="img" aria-label="Line-art ornament of olive branches, grapes, rosemary, a bottle and scrolls framing the label">
        <ellipse cx="404" cy="605" rx="188" ry="180" fill="url(#ornament-fill)"/>
        <ellipse cx="404" cy="405" rx="130" ry="78" fill="url(#ornament-fill)"/>
        <ellipse cx="404" cy="810" rx="150" ry="82" fill="url(#ornament-fill)"/>
      </g>

      <text class="arc-heading" font-family="Josefin Sans, sans-serif" font-weight="600" font-size="13.5" letter-spacing="1" fill="#c9a862">
        <textPath href="#top-arc" startOffset="50%" text-anchor="middle">HUILE D'OLIVE VIERGE EXTRA - AOC HAUTE PROVENCE</textPath>
      </text>

      <circle class="emblem" cx="404" cy="397" r="36" fill="#c9a862"/>
      <circle cx="404" cy="397" r="41" fill="none" stroke="#c9a862" stroke-width="1.5"/>

      <g class="brand-name" font-family="Josefin Sans, sans-serif" font-weight="600" fill="#c9a862" text-anchor="middle">
        <text x="404" y="552" font-size="74" letter-spacing="4">LE</text>
        <text x="404" y="628" font-size="58" letter-spacing="2">HAUT</text>
        <text x="404" y="704" font-size="58" letter-spacing="1">VERGER</text>
      </g>

      <g class="ribbons" fill="#c9a862">
        <path d="M 262 770 Q 300 820 355 838 L 365 818 Q 318 800 288 760 Z"/>
        <path d="M 546 770 Q 508 820 453 838 L 443 818 Q 490 800 520 760 Z"/>
        <path d="M 300 748 L 322 770 L 300 790 L 330 790 Z" fill="#8d6a32"/>
        <path d="M 508 748 L 486 770 L 508 790 L 478 790 Z" fill="#8d6a32"/>
        <path d="M 318 760 Q 404 776 490 760 L 490 794 Q 404 810 318 794 Z"/>
      </g>
      <text x="404" y="792" font-family="Josefin Sans, sans-serif" font-weight="600" font-size="15" letter-spacing="1" fill="#000" text-anchor="middle">LIMITED EDITION</text>
      <text font-family="Josefin Sans, sans-serif" font-weight="600" font-size="11" letter-spacing="1" fill="#000">
        <textPath href="#artisanal-path" startOffset="50%" text-anchor="middle">ARTISANAL</textPath>
      </text>
      <text font-family="Josefin Sans, sans-serif" font-weight="600" font-size="11" letter-spacing="1" fill="#000">
        <textPath href="#unfiltered-path" startOffset="50%" text-anchor="middle">UNFILTERED</textPath>
      </text>

      <text class="arc-footer" font-family="Josefin Sans, sans-serif" font-size="13" letter-spacing="1.2" fill="#e8e6e1">
        <textPath href="#bottom-arc" startOffset="50%" text-anchor="middle">ORGANIC ○ HAND PICKED ○ LATE HARVEST</textPath>
      </text>
    </svg>
  </section>

  <section class="back-label" aria-label="Back label">
    <div class="back-ornament top" role="img" aria-label="Line-art scroll and olive leaf corner ornaments"></div>
    <header class="back-brand">
      <span class="mark" aria-hidden="true"></span>
      <div class="name">LE HAUT VERGER</div>
      <div class="origin">MADE IN FRANCE</div>
    </header>

    <h2 class="story-title">THE STORY ABOUT THIS BOTTLE</h2>

    <p class="story-body">
      Nested in the hills of Provence,<br>
      Le Haut Verger is a wild and magical place<br>
      where forest opens up to vineyards and olive<br>
      groves. We fell in love with it, and you would<br>
      too! It's in these hills that Aglandau olives<br>
      were grown since Roman times, and we were<br>
      happy to bring them back. Our production is<br>
      entirely organic, we pick our olives by hand<br>
      and only at the point of maturity. We don't<br>
      harvest our Aglandaus until very late in the<br>
      autumn, and use a single mechanical<br>
      cold-press extraction. The reward? A very<br>
      special extra virgin oil with its full-on bold<br>
      taste, hints of artichokes and fresh-cut<br>
      grass, and remarkably low acidity.
    </p>

    <p class="meta date">November 2018</p>
    <p class="meta best-before">Best enjoyed before<br>August 2020</p>
    <p class="meta contact">Do let us know how you<br>liked it at info@lehautverger.com</p>
    <p class="meta volume">VOL. 500 ML<br>BOTTLE NO.</p>

    <div class="back-ornament bottom" role="img" aria-label="Line-art scroll, leaf and grape ornament closing the back label"></div>
  </section>

</main>
</body>
</html>
```